Website for Community Storage Startup Company

We're looking for a great design that looks good on mobile devices (as well as the web) - Layout should be responsive and able to scale to many sized devices.

It should provide a good user-experience for people browsing the site with heavy focus on search and search results pages - It should be extremely easy to search, see results and add your own information.

Search parameters should be Location (Text), Dates (Calendar pop up), Price (slider) with optional extra parameters to be displayed (You can just call them Parameter1, Parameter2 etc. for Examples- we'd like to see options of no extra parameters and up to 4 others)

Please include a favicon for the site - we've provided the logo we had designed.

Pages We Must Have:

1) Home Page
2) Search Page (most likely map based)
3) Search Results Page (most likely map based) - we want the search options/results to slide in and out as appropriate - please visualize
Information Page - this is branded and would present information for many possible pages like Terms & Conditions or a FAQ page etc.
4) My Account Page - Should be an inline editable page with Name/Address/Financial information etc. showing
5) Sign-up Page - This could be a slide in element on another page or part of the account page, or separate as you think works best

Ideally this would all work like a single page app with a common theme but we're interested to see your ideas of tying pages together or keeping them separate while fitting our brief.

Examples of things we like;

a) roostly - mobile and web based layouts - we like the map on the side and data input on the other side
b) http://www.zu-o.com/zo/airlines/ - scroll down slightly to the first video - about 0:28 in we like the map on the side and the panel on the side with details you can refine etc. All over we like the site presented through the video

Nice to Have:
- The ability to provide the finished design as sliced CSS, HTML and JS

Reason: Feedback has suggested that the timeline is too tight, we've extended it but are very interested in seeing initial page designs sooner rather than later to provide feedback. Thanks!

Thanks for your contributions so far :)  We've come to realize that in general we're preferring darker color schemes - if you're pulling colors from our logo try to stick to the text colors :)

We like narrow headers and footers and a map based interface. Sliders for information are good and we'd like to see how checkbox elements would play out too.

Examples of how information may pop up from markers would be nice too.

Thanks for everything so far!

Target Market(s)

Young to middle aged adults in the USA

Industry/Entity Type

Airlines

Font styles to use
Sans Serif

Colors

Designer to choose colors to be used in the design.

Requirements
Must have
• 1) Home Page
Nice to have
• The ability to provide the finished design as sliced CSS, HTML and JS

We think a map with markers should figure heavily in search results and searching.

```html
<!DOCTYPE html>
<html lang="en">
<head>
<meta charset="utf-8">
<title>StashLoop – Search</title>
<link href="https://fonts.googleapis.com/css2?family=Roboto:wght@300;400&display=swap" rel="stylesheet">
<style>
  :root {
    --page-bg: #ffffff;
    --panel-bg: #242424;
    --header-bg: #221f20;
    --accent: #45c3d3;
    --text: #ffffff;
    --text-soft: #e6e6e6;
    --rule: #8a8a8a;
    --map-water: #a9c9f2;
    --map-land: #d9e4c4;
  }
  * { box-sizing: border-box; margin: 0; padding: 0; }
  html, body {
    width: 1200px; height: 1000px; overflow: hidden;
    background: var(--page-bg);
    font-family: "Roboto", Arial, sans-serif;
    font-weight: 300;
    color: var(--text);
  }
  .app {
    position: absolute; left: 328px; top: 10px;
    width: 510px; height: 980px;
    background: var(--panel-bg);
  }
  .app-header {
    position: absolute; left: 0; top: 0; width: 510px; height: 67px;
    background: var(--header-bg);
  }
  .brand {
    position: absolute; left: 51px; top: 12px;
    font-size: 34px; font-weight: 300; letter-spacing: 1px;
    color: var(--text);
  }
  .header-rule {
    position: absolute; left: 51px; top: 66px; width: 396px; height: 2px;
    background: var(--accent);
  }
  .search-field {
    position: absolute; left: 53px; width: 394px; height: 42px;
    border-bottom: 1px solid var(--rule);
    display: flex; align-items: center;
    font-size: 18px; color: var(--text);
  }
  .search-field .icon {
    width: 24px; height: 24px; margin-left: 17px; margin-right: 20px;
    display: flex; align-items: center; justify-content: center;
  }
  .search-field .icon svg { fill: var(--text); }
  .btn-search {
    position: absolute; left: 53px; top: 256px; width: 395px; height: 50px;
    background: var(--accent);
  }
  .btn-search span {
    position: absolute; inset: 5px;
    border: 1.5px solid var(--text);
    display: flex; align-items: center; justify-content: center;
    font-size: 15px; font-weight: 400;
  }
  .results-map {
    position: absolute; left: 54px; top: 318px; width: 394px; height: 241px;
    background: linear-gradient(160deg, var(--map-water) 0%, var(--map-land) 35%, var(--map-land) 70%, var(--map-water) 100%);
  }
  .results-label {
    position: absolute; left: 76px; top: 575px;
    font-size: 14px; font-weight: 400; color: var(--accent);
  }
  .result-bar {
    position: absolute; left: 54px; width: 393px; height: 46px;
    background: var(--accent);
    display: flex; align-items: center; justify-content: center;
    font-size: 14px; font-weight: 400; color: var(--text);
  }
  .result-detail {
    position: absolute; left: 54px; width: 393px; height: 42px;
    border-bottom: 1px solid var(--rule);
    display: flex; align-items: center; padding-left: 25px;
    font-size: 16px; color: var(--text-soft);
  }
</style>
</head>
<body>
  <main class="app">
    <header class="app-header">
      <div class="brand">StashLoop</div>
    </header>
    <div class="header-rule"></div>

    <div class="search-field" style="top:72px">
      <span class="icon">
        <svg width="22" height="22" viewBox="0 0 22 22"><path d="M1 8 L11 1 L21 8 V21 H1 Z M5 12 V21 H17 V12 Z"/><rect x="7" y="14" width="3" height="2"/><rect x="11" y="14" width="3" height="2"/><rect x="7" y="17" width="3" height="2"/><rect x="11" y="17" width="3" height="2"/></svg>
      </span>
      Search object
    </div>
    <div class="search-field" style="top:115px">
      <span class="icon">
        <svg width="22" height="22" viewBox="0 0 22 22"><path d="M2 4 H20 V21 H2 Z M4 9 V19 H18 V9 Z"/><rect x="5" y="1" width="2" height="5"/><rect x="15" y="1" width="2" height="5"/><rect x="5" y="10" width="3" height="2"/><rect x="9.5" y="10" width="3" height="2"/><rect x="14" y="10" width="3" height="2"/><rect x="5" y="13.5" width="3" height="2"/><rect x="9.5" y="13.5" width="3" height="2"/><rect x="14" y="13.5" width="3" height="2"/><rect x="5" y="17" width="3" height="1.5"/><rect x="9.5" y="17" width="3" height="1.5"/></svg>
      </span>
      Dates
    </div>
    <div class="search-field" style="top:158px">
      <span class="icon">
        <svg width="24" height="14" viewBox="0 0 24 14"><path d="M1 2 L12 12 L23 2" fill="none" stroke="#ffffff" stroke-width="1.5"/></svg>
      </span>
      Price
    </div>
    <div class="search-field" style="top:201px">
      <span class="icon">
        <svg width="18" height="24" viewBox="0 0 18 24"><path d="M9 0 C4 0 0 4 0 9 C0 15 9 24 9 24 C9 24 18 15 18 9 C18 4 14 0 9 0 Z M9 5 A4 4 0 1 0 9 13 A4 4 0 1 0 9 5 Z" fill-rule="evenodd"/></svg>
      </span>
      Location
    </div>

    <div class="btn-search"><span>SEARCH</span></div>

    <div class="results-map" role="img" aria-label="Map of North America with storage location markers"></div>

    <div class="results-label">SEARCH RESULTS</div>

    <div class="result-bar" style="top:603px">SEARCH OBJECT 1</div>
    <div class="result-detail" style="top:651px">Date</div>
    <div class="result-detail" style="top:693px">Price</div>
    <div class="result-detail" style="top:735px;padding-left:21px">Location</div>
    <div class="result-bar" style="top:785px">SEARCH OBJECT 2</div>
    <div class="result-bar" style="top:836px">SEARCH OBJECT 3</div>
  </main>
</body>
</html>
```